"VEX" Web Design Project

We need a create a webpage for a Streaming device product with sucription that we're going lo launch(like a lumo or pebble tv but comes with a possibily of monthly sucription of live tv channels).
The name of the product is "VEX" (vivid exchange viewing)

We are looking for something simple and with quality. Something webpages that we like are www.skyrune.com www.tindle.tv (our product will be very similar to tindle so you canuse for the menu an information reference, we're going to be more features because we are based on orbix so users can download all the apps from the marlow appmarket)
Also our remote control are gyroscopic (means like the zep remote) for many games.
We are working also in the logo so you can also see in our package and logo contest named: "HOME CAST UNIT: Box-unit-emblem" the Design #: 1768146 are the logo that maybe we're going to choose.

this is the link of our manufacturer to have on idea of the features of the device;
http://www.varnolux.com/pa/qbx730.asp

We like one color on the logo. But we want to see the logo in this colors: white,black ,light blue.

Thanks

Hi,
you can use for reference the TINDLE.TV webpage (look and feel, conten, information and & of pages..) also skyrune.tv as (look & feel).

Information to add:
In the case of the content the basic different is our device is orbix based. So only for reference of information to add (because we don't like lood and feel!!)  please use the info of  this links:

Spanish:
http://www.tolvaro.es/
products:
http://www.tolvaro.es/tolvaro-ZK830.html
http://www.tolvaro.es/descargas.html
http://www.tolvaro.es/about.html
http://www.tolvaro.es/contact.html
http://www.tolvaro.es/distribuidores.html

English:
http://www.tolvaro.com/product.asp?id=166
http://www.tolvaro.com/news.asp
http://www.tolvaro.com/support.asp
http://www.tolvaro.com/where-to-buy.asp
http://www.tolvaro.com/down.asp?id=1
http://www.tolvaro.com/about-us.asp

Note: are the same info but we're going to have only one model called: "VEX" . So we're going to by the devices to this manufacturer but we're going to rebranded...

AGAIN WE DON'T LIKE THE LOOK & FEEL OF THE LAST LINKS (ARE HORRIBLE) PLEASE USE AS A REFRENCE OF "LOOK & FEEL"  WWW.TINDLE.TV OR SKYRUNE.COM

https://www.filecrate-demo.net/sh/qx8831pwwr7mbel/R29KdTesoq

This files can help for the branding and pictures

Can you change the photos of the Slatex's per someone looking TV? One of the advantage of our product vrs conventional tv cable service is that we are Unplugged , we are Cord cutters. With our VEX device people can see TV on their home, their office, their vacation home. Because they can tke with them our device and conect to the internet and can see TV. 
Another advantage if for exmple our partnership with http://www.castorelay.tv/ so people can use their smartphones and tables as a remote control. But not normal remote control, totally interactive remote control and can share also all the network, my phone, and internet content to the TV by our VEX device. 

Please see the attached file. you can use something similar...

Target Market(s)

under 40 years. young people.

Industry/Entity Type

Tv

```html
<!DOCTYPE html>
<html lang="en">
<head>
<meta charset="utf-8">
<title>VEX – Vivid exchange Viewing</title>
<link rel="stylesheet" href="https://fonts.googleapis.com/css2?family=Source+Sans+3:ital,wght@0,400;0,600;1,400;1,600&display=swap">
<style>
:root{
  --blue:#16a3e3;
  --blue-dark:#0c83c7;
  --title-blue:#1b8fd6;
  --navy:#071a2c;
  --black:#050607;
  --panel:rgba(226,231,240,.86);
  --text:#1d1f24;
  --card-text:#3b3f47;
  --footer:#272727;
  --footer-text:#f2f2f2;
  --tweet-box:#4a4a4a;
}
*{box-sizing:border-box;margin:0;padding:0}
html,body{width:1008px;height:1200px;overflow:hidden}
body{position:relative;background:var(--navy);font-family:"Source Sans 3",Arial,sans-serif;color:var(--text)}
.abs{position:absolute}
/* header */
.top-bar{left:0;top:0;width:1008px;height:38px;background:var(--black)}
.header{left:0;top:38px;width:1008px;height:48px;background:linear-gradient(#0b1624,#0a2036)}
.header-rule{left:0;top:86px;width:1008px;height:3px;background:var(--blue)}
.logo{left:92px;top:15px;height:60px;display:flex;align-items:center;gap:8px;color:var(--blue);font-weight:600;font-size:44px;letter-spacing:2px}
.logo .dot{width:34px;height:34px;border-radius:50%;background:var(--blue)}
.nav{left:514px;top:29px;display:flex;align-items:center;font-size:14.5px;color:#fff}
.nav a{color:#fff;text-decoration:none;height:29px;line-height:29px;margin-right:25px}
.nav a.active{background:var(--blue);padding:0 11px;margin-right:14px}
.join{left:732px;top:89px;width:162px;height:37px;background:var(--blue);color:#fff;font-size:15.5px;text-align:center;line-height:37px}
/* hero */
.hero-bg{left:0;top:89px;width:1008px;height:852px;background:
  radial-gradient(ellipse at 50% 60%,rgba(40,170,200,.45),transparent 60%),
  linear-gradient(#0a2a44 0%,#0f3f5e 30%,#1b6a86 55%,#0d3b55 80%,#0a2236 100%)}
.hero-title{left:104px;top:196px;font-size:40px;color:#fff;font-weight:400}
.hero-sub{left:103px;top:256px;font-size:25px;color:#fff}
.buy{left:105px;top:313px;width:168px;height:45px;background:linear-gradient(var(--blue),var(--blue-dark));color:#fff;font-size:23px;line-height:45px;text-align:center}
.slider-arrows{left:103px;top:394px}
.device{left:487px;top:139px;width:429px;height:285px}
/* intro */
.intro{left:84px;top:449px;width:840px;height:136px;background:var(--panel)}
.intro h1{position:absolute;left:31px;top:12px;font-size:27px;font-style:italic;font-weight:400;color:var(--title-blue)}
.intro p{position:absolute;left:36px;top:55px;width:760px;font-size:12.6px;line-height:25px;color:var(--text)}
.btn{display:flex;align-items:center;justify-content:center;gap:8px;background:linear-gradient(var(--blue),var(--blue-dark));color:#fff;font-size:12.5px}
.btn .go{width:17px;height:17px;border-radius:50%;background:#fff;display:flex;align-items:center;justify-content:center}
.register{position:absolute;left:668px;top:96px;width:124px;height:27px}
/* cards */
.card{top:600px;width:274px;height:223px;background:var(--panel)}
.card h2{position:absolute;left:20px;top:10px;font-size:27px;font-style:italic;font-weight:400;color:var(--title-blue)}
.card svg.icon{position:absolute;right:18px;top:10px}
.card p{position:absolute;left:18px;top:58px;width:240px;font-size:10.8px;line-height:20px;text-align:justify;color:var(--card-text)}
.card .more{position:absolute;left:14px;top:181px;width:110px;height:27px}
/* partners */
.partners{left:86px;top:833px;width:838px;height:91px;background:rgba(214,218,224,.9);display:flex;align-items:center;justify-content:space-around;padding:0 60px;color:#6a6d72;font-size:17px;font-weight:600}
/* footer */
.footer{left:0;top:941px;width:1008px;height:259px;background:var(--footer);color:var(--footer-text)}
.footer h3{position:absolute;font-size:14.5px;font-weight:400;color:#fff}
.links{position:absolute;top:50px;list-style:none;font-size:11px;font-weight:600;line-height:23.5px}
.links li::before{content:"• ";font-size:9px}
.news-input{position:absolute;left:391px;top:57px;width:234px;height:29px;background:#fff;border-radius:15px;display:flex;align-items:center;gap:7px;padding-left:12px;font-size:11px;color:#8a8a8a}
.news-caption{position:absolute;left:391px;top:96px;width:234px;text-align:right;font-size:12px;font-weight:600;color:#fff}
.subscribe{position:absolute;left:512px;top:124px;width:124px;height:30px;background:linear-gradient(var(--blue),var(--blue-dark));color:#fff;font-size:15px;font-weight:600;text-align:center;line-height:30px}
.tweet{position:absolute;left:690px;top:63px;width:194px;height:97px;background:var(--tweet-box);border-radius:5px;padding:17px 16px;font-size:10.5px;line-height:16px}
.tweet-mark{position:absolute;left:822px;top:26px;width:26px;height:26px;border-radius:50%;background:var(--blue)}
.copyright{position:absolute;left:113px;top:210px;display:flex;align-items:center;gap:10px;font-family:Arial,sans-serif;font-size:10.5px;color:#fff}
.copyright .mini-logo{font-family:"Source Sans 3",sans-serif;font-size:20px;font-weight:600;color:#666;letter-spacing:1px}
.social{position:absolute;left:715px;top:198px;display:flex;gap:9px}
.social span{width:26px;height:26px;border-radius:50%;background:#fff;display:flex;align-items:center;justify-content:center}
</style>
</head>
<body>
  <div class="abs top-bar"></div>
  <div class="abs header"></div>
  <div class="abs header-rule"></div>
  <div class="abs logo"><span class="dot"></span>VEX</div>
  <nav class="abs nav">
    <a class="active" href="#">Home</a><a href="#">How it works</a><a href="#">TV Channels</a><a href="#">Plans</a><a href="#">Support</a>
  </nav>

  <div class="abs hero-bg" role="img" aria-label="Night city skyline photo with lit towers along a river"></div>
  <div class="abs join">Join now&nbsp; / &nbsp;Sign up</div>
  <h1 class="abs hero-title">Welcome to VEX</h1>
  <div class="abs hero-sub">Vivid exchange Viewing</div>
  <div class="abs buy">BUY NOW</div>
  <svg class="abs slider-arrows" width="72" height="32" viewBox="0 0 72 32">
    <circle cx="15" cy="16" r="15" fill="rgba(120,130,140,.55)"/>
    <path d="M18 10 L11 16 L18 22Z" fill="#1da1e0"/>
    <circle cx="52" cy="16" r="15" fill="rgba(120,130,140,.55)"/>
    <path d="M49 10 L56 16 L49 22Z" fill="#1da1e0"/>
  </svg>
  <svg class="device abs" viewBox="0 0 429 285" role="img" aria-label="Tablet showing the VEX TV app home screen with app tiles">
    <defs><linearGradient id="scr" x1="0" y1="0" x2="1" y2="1"><stop offset="0" stop-color="#2a2f36"/><stop offset="1" stop-color="#0c0e11"/></linearGradient></defs>
    <path d="M90 15 L425 0 L345 285 L0 250Z" fill="url(#scr)" stroke="#55595f" stroke-width="3"/>
  </svg>

  <section class="abs intro">
    <h1>VEX - Vivid exchange Viewing</h1>
    <p>Sed ut perspiciatis unde omnis iste natus error sit voluptatem accusantium doloremque laudantium, totam rem aperiam, eaque ipsa quae ab illo inventore veritatis et quasi architecto beatae vitae dicta sunt explicabo. Nemo enim ipsam voluptatem quia</p>
    <div class="btn register">REGISTER NOW <span class="go"><svg width="8" height="8"><path d="M2 0 L7 4 L2 8Z" fill="#0c83c7"/></svg></span></div>
  </section>

  <article class="abs card" style="left:86px">
    <h2>About Us</h2>
    <svg class="icon" width="38" height="32" viewBox="0 0 38 32"><circle cx="13" cy="8" r="6" fill="#1b8fd6"/><circle cx="26" cy="8" r="6" fill="#1b8fd6"/><path d="M1 28 Q13 10 25 28Z M14 28 Q26 10 37 28Z" fill="#1b8fd6"/></svg>
    <p>Sed ut perspiciatis unde omnis iste natus error sit voluptatem accusantium doloremque laudantium, totam rem aperiam, eaque ipsa quae ab illo inventore veritatis et quasi architecto beatae vitae dicta sunt explicabo. Nemo enim ipsam voluptatem quia voluptas</p>
    <div class="btn more">VIEW MORE <span class="go"><svg width="8" height="8"><path d="M2 0 L7 4 L2 8Z" fill="#0c83c7"/></svg></span></div>
  </article>
  <article class="abs card" style="left:368px">
    <h2>How it Works</h2>
    <svg class="icon" width="38" height="32" viewBox="0 0 38 32"><rect x="5" y="3" width="28" height="20" rx="2" fill="none" stroke="#1b8fd6" stroke-width="2.5"/><rect x="1" y="25" width="36" height="4" rx="2" fill="#1b8fd6"/><circle cx="19" cy="12" r="4" fill="none" stroke="#1b8fd6" stroke-width="2"/></svg>
    <p>Sed ut perspiciatis unde omnis iste natus error sit voluptatem accusantium doloremque laudantium, totam rem aperiam, eaque ipsa quae ab illo inventore veritatis et quasi architecto beatae vitae dicta sunt explicabo. Nemo enim ipsam voluptatem quia voluptas</p>
    <div class="btn more">VIEW MORE <span class="go"><svg width="8" height="8"><path d="M2 0 L7 4 L2 8Z" fill="#0c83c7"/></svg></span></div>
  </article>
  <article class="abs card" style="left:649px">
    <h2>Support</h2>
    <svg class="icon" width="36" height="34" viewBox="0 0 36 34"><circle cx="18" cy="15" r="7" fill="#1b8fd6"/><rect x="14" y="23" width="8" height="6" fill="#1b8fd6"/><g stroke="#1b8fd6" stroke-width="2.5"><path d="M18 1v4M3 15h4M29 15h4M7 4l3 3M29 4l-3 3"/></g></svg>
    <p>Sed ut perspiciatis unde omnis iste natus error sit voluptatem accusantium doloremque laudantium, totam rem aperiam, eaque ipsa quae ab illo inventore veritatis et quasi architecto beatae vitae dicta sunt explicabo. Nemo enim ipsam voluptatem quia voluptas</p>
    <div class="btn more">VIEW MORE <span class="go"><svg width="8" height="8"><path d="M2 0 L7 4 L2 8Z" fill="#0c83c7"/></svg></span></div>
  </article>

  <div class="abs partners">
    <span>Tallymark</span><span>Cuponette</span><span>Brightsheaf</span><span>Fernplum</span><span>Emberlane</span><span>Keptcoin</span>
  </div>

  <footer class="abs footer">
    <h3 style="left:115px;top:2px">Quick Links</h3>
    <ul class="links" style="left:116px"><li>Integer lobortis</li><li>Curabitur ac</li><li>Phasellus tellus nisl</li><li>Aenean fringilla</li><li>Vestibulum</li><li>Aliquam commodo</li></ul>
    <ul class="links" style="left:260px"><li>Integer lobortis</li><li>Curabitur ac</li><li>Phasellus tellus nisl</li><li>Aenean fringilla</li><li>Vestibulum</li><li>Aliquam commodo</li></ul>
    <h3 style="left:386px;top:2px">Newsletter</h3>
    <div class="news-input"><svg width="19" height="13"><rect x=".5" y=".5" width="18" height="12" fill="none" stroke="#888"/><path d="M1 1 L9.5 8 L18 1" fill="none" stroke="#888"/></svg>Subscribe your news letter</div>
    <div class="news-caption">Subscribe your news letter</div>
    <div class="subscribe">SUBSCRIBE</div>
    <h3 style="left:690px;top:13px">Chirplet Updates</h3>
    <div class="tweet-mark"></div>
    <div class="tweet">@lunathemes there is a new designer in town people!<br><br>Check it out: http://qk.vx/urds</div>
    <div class="copyright"><span class="mini-logo">VEX</span><span>Copyright &nbsp;© &nbsp;2013 &nbsp;&nbsp;www.vex-vividexchangeviewing.com &nbsp;All rights reserved.</span></div>
    <div class="social"><span></span><span></span><span></span><span></span><span><svg width="14" height="14"><path d="M5 0h4v5h5v4H9v5H5V9H0V5h5z" fill="#272727"/></svg></span></div>
  </footer>
</body>
</html>
```